Automotive Accessories Business Card

Design a business template that match our new logo design and our industry.

https://www.kelvramotive.com/

Target Market(s)

Aftermarket auto parts and accessories

Industry/Entity Type

automotive

Contact Information for Business Card

company logo

Font styles to use
Serif
Sans Serif

Colors
EB3D1F
EC4F4E
F09395
F8D3D4
FCEDEE

```html
<!DOCTYPE html>
<html lang="en">
<head>
<meta charset="utf-8">
<title>Kelvra Motive – Business Card</title>
<link href="https://fonts.googleapis.com/css2?family=Roboto:wght@400;500;700&display=swap" rel="stylesheet">
<style>
  :root {
    --backdrop: #c9c8c9;
    --card-white: #ffffff;
    --red-top: #cf1f26;
    --red-bottom: #8e0c12;
    --ink: #1d1d1f;
    --ink-dark: #3a3a3c;
    --accent: #e0232b;
    --paper-text: #ffffff;
  }
  * { box-sizing: border-box; margin: 0; padding: 0; }
  html, body {
    width: 707px;
    height: 1200px;
    overflow: hidden;
    background: var(--backdrop);
    font-family: "Roboto", Arial, sans-serif;
  }
  .sheet {
    width: 707px;
    height: 1200px;
    display: flex;
    flex-direction: column;
    align-items: center;
    justify-content: center;
    gap: 40px;
  }
  .card {
    width: 560px;
    height: 320px;
    position: relative;
    box-shadow: 0 6px 18px rgba(0,0,0,0.25);
  }
  .card--front { background: var(--card-white); }
  .card--back {
    background: linear-gradient(180deg, var(--red-top) 0%, var(--red-bottom) 100%);
    display: flex;
    flex-direction: column;
    align-items: center;
    justify-content: center;
  }
  .brand {
    display: flex;
    align-items: center;
    gap: 12px;
    font-weight: 700;
    font-size: 36px;
    letter-spacing: 0.5px;
    color: var(--ink-dark);
  }
  .brand__mark {
    width: 22px;
    height: 22px;
    background: var(--accent);
    flex: none;
  }
  .card--front .brand {
    position: absolute;
    left: 72px;
    top: 96px;
  }
  .card--back .brand {
    color: var(--paper-text);
    font-size: 40px;
    margin-bottom: 52px;
  }
  .card--back .brand__mark { background: var(--paper-text); }
  .contact {
    position: absolute;
    left: 80px;
    top: 190px;
    list-style: none;
    display: flex;
    flex-direction: column;
    gap: 6px;
  }
  .contact__item {
    display: flex;
    align-items: center;
    gap: 10px;
    font-size: 13px;
    color: var(--ink);
  }
  .contact__icon { width: 26px; height: 20px; flex: none; }
  .services {
    display: flex;
    flex-direction: column;
    align-items: center;
    gap: 14px;
    color: var(--paper-text);
    font-weight: 500;
    font-size: 13px;
    text-transform: uppercase;
  }
  .services__row {
    list-style: none;
    display: flex;
    justify-content: center;
    gap: 20px;
  }
</style>
</head>
<body>
<main class="sheet">
  <section class="card card--front" aria-label="Business card front">
    <div class="brand"><span class="brand__mark"></span>Kelvra Motive</div>
    <ul class="contact">
      <li class="contact__item">
        <svg class="contact__icon" viewBox="0 0 26 20" aria-hidden="true">
          <polygon points="13,1 25,19 1,19" fill="#2a2a2c"/>
          <path d="M10.5 10.5 q1 3 4.5 4.5 l1.2-1.2 -1.6-1 -0.8 0.6 q-1.4-0.8-2-2 l0.6-0.8 -1-1.6z" fill="#fff"/>
        </svg>1-800-555-0142</li>
      <li class="contact__item">
        <svg class="contact__icon" viewBox="0 0 26 20" aria-hidden="true">
          <polygon points="13,1 25,19 1,19" fill="#2a2a2c"/>
          <rect x="9.5" y="11" width="7" height="5" fill="#fff"/>
          <path d="M9.5 11 l3.5 2.6 3.5-2.6" stroke="#2a2a2c" stroke-width="0.8" fill="none"/>
        </svg>sales@kelvramotive.com</li>
      <li class="contact__item">
        <svg class="contact__icon" viewBox="0 0 26 20" aria-hidden="true">
          <polygon points="13,1 25,19 1,19" fill="#2a2a2c"/>
          <circle cx="13" cy="13.5" r="3.4" fill="none" stroke="#fff" stroke-width="0.9"/>
          <path d="M9.6 13.5 h6.8 M13 10.1 v6.8" stroke="#fff" stroke-width="0.7"/>
        </svg>www.kelvramotive.com</li>
    </ul>
  </section>

  <section class="card card--back" aria-label="Business card back">
    <div class="brand"><span class="brand__mark"></span>Kelvra Motive</div>
    <div class="services">
      <ul class="services__row">
        <li>Fender Trim</li>
        <li>Hitch</li>
        <li>Grilles</li>
        <li>Running Boards</li>
      </ul>
      <ul class="services__row">
        <li>Off-Road</li>
        <li>Truck Armor</li>
        <li>Fernder Flare</li>
      </ul>
    </div>
  </section>
</main>
</body>
</html>
```